Business card design needed

It's a new business in town.Something so the name stands out.I need a logo for the B.R.W
I may all so use the design as a sign on a building

Contact Information for Business Card

B.R.W
Brindlewood Auto Detailing
42 Fenwarra Crs
Brindlewood Vic 3799
Ph:(03)59284736
Mob:0417362958

```html
<!DOCTYPE html>
<html lang="en">
<head>
<meta charset="utf-8">
<title>Brindlewood Auto Detailing – Business Card</title>
<link rel="stylesheet" href="https://fonts.googleapis.com/css2?family=Montserrat:wght@500;600&family=Open+Sans:wght@400&display=swap">
<style>
  :root {
    --stage-blue: #00a8ec;
    --card-black: #000000;
    --panel-white: #ffffff;
    --accent-blue: #1fa6e3;
    --brand-blue: #3aaee6;
    --text-grey: #6b6b6b;
    --steel-dark: #1a1a1a;
    --steel-light: #b4b4b8;
    --mesh-grey: #3a3a3a;
  }
  html, body {
    margin: 0;
    padding: 0;
    width: 1200px;
    height: 900px;
    overflow: hidden;
    background: var(--stage-blue);
  }
  .canvas {
    position: relative;
    width: 1200px;
    height: 900px;
    background: var(--stage-blue);
  }
  .card {
    position: absolute;
    left: 230px;
    width: 742px;
    background: var(--card-black);
    overflow: hidden;
  }
  .card--front { top: 15px; height: 428px; }
  .card--back  { top: 457px; height: 428px; }

  .front-header {
    position: absolute;
    left: 0; top: 0;
    width: 742px; height: 198px;
    background: var(--card-black);
  }
  .mesh-texture {
    position: absolute;
    right: 0; top: 0;
    width: 480px; height: 198px;
    background:
      radial-gradient(ellipse at 85% 30%, rgba(90,90,90,0.55), rgba(0,0,0,0) 70%),
      linear-gradient(90deg, rgba(0,0,0,1) 0%, rgba(40,40,40,0.6) 45%, var(--mesh-grey) 100%);
  }
  .brand-name {
    position: absolute;
    left: 100px; top: 48px;
    margin: 0;
    font-family: "Montserrat", sans-serif;
    font-weight: 600;
    font-size: 80px;
    line-height: 1;
    letter-spacing: 2px;
    color: var(--brand-blue);
  }
  .brand-tagline {
    position: absolute;
    left: 42px; top: 136px;
    margin: 0;
    font-family: "Montserrat", sans-serif;
    font-weight: 500;
    font-size: 21px;
    font-variant: small-caps;
    letter-spacing: 3.2px;
    color: var(--panel-white);
    white-space: nowrap;
  }
  .rule-white {
    position: absolute;
    left: 0; top: 198px;
    width: 742px; height: 3px;
    background: var(--panel-white);
  }
  .steel-bar {
    position: absolute;
    left: 0;
    width: 742px;
    background: linear-gradient(90deg, var(--steel-dark) 0%, #5a5a5c 30%, var(--steel-light) 50%, #5a5a5c 70%, var(--steel-dark) 100%);
  }
  .steel-bar--thin { top: 201px; height: 12px; }
  .steel-bar--wide { top: 395px; height: 33px; }

  .contact-panel {
    position: absolute;
    left: 0; top: 213px;
    width: 742px; height: 182px;
    background: var(--panel-white);
    font-family: "Open Sans", sans-serif;
    color: var(--text-grey);
  }
  .contact-line {
    position: absolute;
    left: 41px;
    margin: 0;
    font-size: 26px;
    letter-spacing: 0.5px;
    white-space: nowrap;
  }
  .contact-line--phone  { top: 40px; }
  .contact-line--mobile { top: 82px; }
  .contact-label { color: var(--accent-blue); }
  .contact-address {
    position: absolute;
    left: 41px; top: 145px;
    margin: 0;
    font-size: 21px;
    white-space: nowrap;
  }

  .back-brand {
    position: absolute;
    left: 0; top: 188px;
    width: 742px;
    margin: 0;
    text-align: center;
    font-family: "Montserrat", sans-serif;
    font-weight: 600;
    font-size: 84px;
    line-height: 1;
    letter-spacing: 2px;
    color: var(--brand-blue);
  }
</style>
</head>
<body>
<main class="canvas">
  <section class="card card--front" aria-label="Business card front">
    <header class="front-header">
      <div class="mesh-texture" role="img" aria-label="Dark hexagonal metal mesh texture"></div>
      <h1 class="brand-name">B.R.W</h1>
      <p class="brand-tagline">Brindlewood Auto Detailing</p>
    </header>
    <div class="rule-white"></div>
    <div class="steel-bar steel-bar--thin"></div>
    <div class="contact-panel">
      <p class="contact-line contact-line--phone"><span class="contact-label">P:</span> (03)59284736</p>
      <p class="contact-line contact-line--mobile"><span class="contact-label">M:</span> 0417362958</p>
      <p class="contact-address">42 Fenwarra Crs Brindlewood Vic 3799</p>
    </div>
    <div class="steel-bar steel-bar--wide"></div>
  </section>

  <section class="card card--back" aria-label="Business card back">
    <p class="back-brand">B.R.W</p>
  </section>
</main>
</body>
</html>
```